Design some Business Cards for Quelvaro

Design some business Cards for my company.

Artwork is included and a sample old business card with the necessary info we must have.
We would like a new more modern look (simple, yet elegant) using our existing logo.

```html
<!DOCTYPE html>
<html lang="es">
<head>
<meta charset="utf-8">
<title>Quelvaro – Tarjetas de presentación</title>
<link href="https://fonts.googleapis.com/css2?family=Montserrat:wght@400;600;700;800&display=swap" rel="stylesheet">
<style>
  :root{
    --backdrop:#3b3b3d;
    --paper:#fbfbfa;
    --gold:#c9a062;
    --gold-deep:#b98d4f;
    --orange:#f5a01f;
    --ink-light:#ffffff;
    --ink-soft:#fff6e8;
    --divider:#b08649;
  }
  *{box-sizing:border-box;margin:0;padding:0}
  html,body{width:1200px;height:749px;overflow:hidden;background:var(--backdrop)}
  body{position:relative;font-family:"Montserrat",sans-serif}
  .card{position:absolute;background:var(--paper);overflow:hidden;box-shadow:0 6px 18px rgba(0,0,0,.35)}
  .brand{display:flex;align-items:center;justify-content:center;gap:10px}
  .brand-mark{width:18px;height:18px;background:var(--gold-deep)}
  .brand-name{font-weight:800;color:var(--orange);letter-spacing:2px}
  .icon{width:14px;height:14px;flex:none}
  .icon path,.icon rect,.icon circle{fill:var(--ink-light)}
  .contact{display:flex;align-items:center;gap:9px;color:var(--ink-light);font-size:11px;line-height:1}

  /* Front card */
  .card-front{left:60px;top:30px;width:580px;height:320px}
  .card-front .brand{position:absolute;left:0;width:440px;top:95px}
  .card-front .brand-name{font-size:44px}
  .card-front .website{position:absolute;left:0;width:440px;top:158px;text-align:center;font-size:19px;font-weight:600;color:#5a4a36;letter-spacing:1.5px}
  .card-front .band{position:absolute;left:0;right:0;bottom:0;height:112px;background:var(--gold)}
  .card-front .holder{position:absolute;left:46px;bottom:32px;color:var(--ink-light)}
  .card-front .contacts{position:absolute;right:44px;top:232px;display:flex;flex-direction:column;gap:10px}
  .holder-name{font-weight:700;font-size:22px}
  .holder-role{font-size:12px;color:var(--ink-soft);margin-top:2px}

  /* Back card */
  .card-back{left:540px;top:370px;width:610px;height:350px;border-top:6px solid var(--orange);border-bottom:6px solid var(--orange)}
  .card-back .brand{position:absolute;left:0;right:0;top:48px}
  .card-back .brand-name{font-size:34px}
  .card-back .band{position:absolute;left:0;right:0;top:128px;height:168px;background:var(--gold)}
  .card-back .divider{position:absolute;left:300px;top:18px;bottom:18px;width:1px;background:var(--divider)}
  .card-back .address{position:absolute;left:38px;top:26px;display:flex;gap:10px;color:var(--ink-light);font-size:10.5px;line-height:1.45}
  .card-back .phones{position:absolute;left:38px;top:96px;display:flex;flex-direction:column;gap:8px}
  .card-back .holder{position:absolute;left:330px;top:22px;color:var(--ink-light)}
  .card-back .holder-name{font-size:21px}
  .card-back .holder-role{text-align:right}
  .card-back .contacts-web{position:absolute;left:360px;top:98px;display:flex;flex-direction:column;gap:10px}
</style>
</head>
<body>

<section class="card card-front">
  <div class="brand"><span class="brand-mark"></span><span class="brand-name">QUELVARO</span></div>
  <p class="website">www.quelvaro.com.pa</p>
  <div class="band"></div>
  <div class="holder">
    <p class="holder-name">Rodrigo A. Salcedo</p>
    <p class="holder-role">Vicepresidente</p>
  </div>
  <div class="contacts">
    <p class="contact"><svg class="icon" viewBox="0 0 14 14"><rect x="4" y="1" width="6" height="12" rx="1"/></svg>507 310 4478</p>
    <p class="contact"><svg class="icon" viewBox="0 0 14 14"><path d="M3 1l3 3-1.5 2a8 8 0 0 0 3.5 3.5L10 8l3 3-2 2C6 13 1 8 1 3z"/></svg>507 310 4465</p>
    <p class="contact"><svg class="icon" viewBox="0 0 14 14"><path d="M1 3h12v8H1zM2 4l5 4 5-4v-.2H2z" fill-rule="evenodd"/></svg>rodrigo@quelvaro.com.pa</p>
  </div>
</section>

<section class="card card-back">
  <div class="brand"><span class="brand-mark"></span><span class="brand-name">QUELVARO</span></div>
  <div class="band">
    <div class="address">
      <svg class="icon" viewBox="0 0 14 14"><path d="M7 0a5 5 0 0 0-5 5c0 4 5 9 5 9s5-5 5-9a5 5 0 0 0-5-5zm0 7a2 2 0 1 1 0-4 2 2 0 0 1 0 4z"/></svg>
      <p>P.H. Torre Ámbar 210, Oficina 7C<br>Calle Olmo, junto a Plaza Norte<br>Ciudad de Panamá, Panamá</p>
    </div>
    <div class="phones">
      <p class="contact"><svg class="icon" viewBox="0 0 14 14"><path d="M3 1l3 3-1.5 2a8 8 0 0 0 3.5 3.5L10 8l3 3-2 2C6 13 1 8 1 3z"/></svg>507 310 4465</p>
      <p class="contact"><svg class="icon" viewBox="0 0 14 14"><rect x="2" y="2" width="10" height="11" rx="1"/></svg>507 310 4478</p>
      <p class="contact"><svg class="icon" viewBox="0 0 14 14"><rect x="4" y="1" width="6" height="12" rx="1"/></svg>507 6245 8831</p>
    </div>
    <div class="divider"></div>
    <div class="holder">
      <p class="holder-name">Rodrigo A. Salcedo</p>
      <p class="holder-role">Vicepresidente</p>
    </div>
    <div class="contacts-web">
      <p class="contact"><svg class="icon" viewBox="0 0 14 14"><path d="M1 3h12v8H1zM2 4l5 4 5-4v-.2H2z" fill-rule="evenodd"/></svg>rodrigo@quelvaro.com.pa</p>
      <p class="contact"><svg class="icon" viewBox="0 0 14 14"><path d="M2 2h10v7H2zM3 3v5h8V3zM1 10h12v2H1z" fill-rule="evenodd"/></svg>www.quelvaro.com.pa</p>
    </div>
  </div>
</section>

</body>
</html>
```